B2B Consulting firm needs a re-fresh of its process diagrams

We are a commercial real estate consulting firm. Think: I wonder who Korvanta uses when they have to build a new plant and sell the old one? That's us! We have created diagrams that we use to demonstrate to our clients the process of the project that they are about to go through. That is our "frontstage" diagram. We also have a "backstage" diagram that we use to train employees and to ensure that we do not make a stupid mistake! Here is a video showing you a little about what we are wanting https://view.clipmarrow.com/v/QpLRZW7BYEK4t8HJ2MVS

Target Market(s)

B2B - C-suite and business leaders

Industry/Entity Type

Commercial Real Estate

Font styles to use
Sans Serif

Colors
0094D4
00A9DD
6FCCEA
C7EBF8
E9F6FB
EB3D1F
EC4F4E
F09395
F8D3D4
FCEDEE

Requirements
Must have
• Think of it as a infographic - clean and modern
Nice to have
• I would suggest that you look at the infographics that are used by Pellingham Trade Journal, Drummoth, TVRL and other professional services firms/publications.

```html
<!DOCTYPE html>
<html lang="en">
<head>
<meta charset="utf-8">
<title>Space Acquisition – Purchase and Process Deliverables</title>
<link href="https://fonts.googleapis.com/css2?family=Montserrat:wght@300;400;600;700;800;900&family=Teko:wght@600&display=swap" rel="stylesheet">
<style>
  :root{
    --red:#c33b25;
    --navy:#2b3a88;
    --title-blue:#0c4f9c;
    --dot-blue:#4a86c5;
    --dot-orange:#e99a0c;
    --head-orange:#f0a000;
    --ink:#1d1d1d;
    --panel-edge:#d4d4d6;
  }
  *{margin:0;padding:0;box-sizing:border-box}
  html,body{width:1200px;height:1200px;overflow:hidden;background:#fff}
  body{position:relative;font-family:"Montserrat",sans-serif;color:var(--ink)}
  .page-title{position:absolute;left:27px;top:174px;line-height:1}
  .page-title .strong{display:block;font-weight:900;font-size:53px;color:var(--navy);letter-spacing:-0.5px}
  .page-title .light{display:block;font-weight:300;font-size:46px;color:var(--red);margin-top:-2px}
  .panel{position:absolute;left:27px;top:311px;width:1156px;height:867px;
    background:radial-gradient(ellipse at 50% 50%,#ffffff 0%,#f4f4f5 45%,var(--panel-edge) 100%);overflow:hidden}
  .flow{position:absolute;left:0;top:0}
  .title-block{position:absolute;right:799px;top:362px;text-align:right;font-family:"Teko",sans-serif;font-weight:600;line-height:0.84}
  .title-block span{display:block;transform:scaleX(0.68);transform-origin:right center;white-space:nowrap}
  .title-block .t-red{color:var(--red);font-size:64px}
  .title-block .t-blue{color:var(--title-blue);font-size:84px;margin-top:-2px}
  .legend{position:absolute;font-weight:700;font-size:13px;white-space:nowrap}
  .blk{position:absolute;font-size:8.5px;line-height:11.3px}
  .nw{white-space:nowrap}
  .role{font-weight:800;font-size:11px;line-height:11px;text-transform:uppercase;margin-bottom:3px;white-space:nowrap}
  .step-head{font-weight:700;font-size:13px;line-height:14px;color:var(--head-orange);margin-bottom:1px}
  .blk ul{list-style:none}
  .blk li::before{content:"• "}
  .deliv{font-weight:700}
  .deliv .n{display:inline-block;width:17px}
  .deliv .ind{padding-left:17px;font-weight:400}
  .actions{font-size:8px;line-height:11px;white-space:nowrap}
  .actions p+p{margin-top:6px}
  .bar{position:absolute;left:499px;top:1106px;width:385px;height:34px;background:var(--red)}
</style>
</head>
<body>
  <h1 class="page-title"><span class="strong">INFOGRAPHIC</span><span class="light">CONCEPT</span></h1>

  <div class="panel"></div>

  <svg class="flow" width="1200" height="1200" viewBox="0 0 1200 1200" aria-hidden="true">
    <g stroke="#c33b25" stroke-width="1.3" fill="none">
      <line x1="452" y1="311" x2="452" y2="694"/>
      <line x1="452" y1="884" x2="452" y2="1178"/>
      <line x1="933" y1="311" x2="933" y2="1178"/>
      <line x1="452" y1="378" x2="933" y2="378"/>
      <line x1="933" y1="516" x2="1183" y2="516"/>
      <line x1="27" y1="694" x2="933" y2="694"/>
      <line x1="107" y1="694" x2="107" y2="1178"/>
      <line x1="107" y1="884" x2="1183" y2="884"/>
      <line x1="597" y1="694" x2="597" y2="884"/>
    </g>
    <g fill="#c33b25">
      <polygon points="671,365 697,378 671,391"/>
      <polygon points="920,432 946,432 933,458"/>
      <polygon points="920,684 946,684 933,710"/>
      <polygon points="459,681 433,694 459,707"/>
      <polygon points="94,785 120,785 107,811"/>
      <polygon points="265,871 291,884 265,897"/>
      <polygon points="584,894 610,894 597,868"/>
      <polygon points="440,983 466,996 440,1009"/>
    </g>
    <g fill="#c33b25">
      <circle cx="452" cy="378" r="31"/><circle cx="933" cy="378" r="31"/>
      <circle cx="933" cy="516" r="31"/><circle cx="933" cy="884" r="31"/>
      <circle cx="594" cy="694" r="31"/><circle cx="107" cy="694" r="31"/>
      <circle cx="107" cy="884" r="31"/><circle cx="452" cy="884" r="31"/>
    </g>
    <g fill="#fff" font-family="Montserrat, sans-serif" font-weight="900" font-size="40" text-anchor="middle">
      <text x="452" y="392">1</text><text x="933" y="392">2</text>
      <text x="933" y="530">3</text><text x="933" y="898">4</text>
      <text x="594" y="708">5</text><text x="107" y="708">6</text>
      <text x="107" y="898">7</text><text x="452" y="898">8</text>
    </g>
    <g fill="#4a86c5">
      <circle cx="207" cy="629" r="8"/>
      <circle cx="511" cy="409" r="8"/><circle cx="533" cy="409" r="8"/><circle cx="555" cy="409" r="8"/>
      <circle cx="990" cy="361" r="8"/><circle cx="1012" cy="361" r="8"/><circle cx="1034" cy="361" r="8"/>
      <circle cx="990" cy="557" r="8"/><circle cx="1012" cy="557" r="8"/><circle cx="1034" cy="557" r="8"/>
      <circle cx="178" cy="730" r="8"/><circle cx="200" cy="730" r="8"/><circle cx="222" cy="730" r="8"/>
      <circle cx="664" cy="730" r="8"/><circle cx="686" cy="730" r="8"/><circle cx="708" cy="730" r="8"/>
      <circle cx="179" cy="921" r="8"/><circle cx="201" cy="921" r="8"/><circle cx="223" cy="921" r="8"/>
      <circle cx="511" cy="921" r="8"/><circle cx="533" cy="921" r="8"/><circle cx="555" cy="921" r="8"/>
      <circle cx="990" cy="921" r="8"/><circle cx="1012" cy="921" r="8"/><circle cx="1034" cy="921" r="8"/>
    </g>
    <g fill="#e99a0c">
      <circle cx="153" cy="650" r="8"/>
      <circle cx="729" cy="409" r="8"/><circle cx="751" cy="409" r="8"/><circle cx="773" cy="409" r="8"/>
      <circle cx="990" cy="441" r="8"/><circle cx="1012" cy="441" r="8"/><circle cx="1034" cy="441" r="8"/>
      <circle cx="990" cy="700" r="8"/><circle cx="1012" cy="700" r="8"/><circle cx="1034" cy="700" r="8"/>
      <circle cx="418" cy="730" r="8"/><circle cx="440" cy="730" r="8"/><circle cx="462" cy="730" r="8"/>
      <circle cx="664" cy="801" r="8"/><circle cx="686" cy="801" r="8"/><circle cx="708" cy="801" r="8"/>
      <circle cx="731" cy="921" r="8"/><circle cx="753" cy="921" r="8"/><circle cx="775" cy="921" r="8"/>
      <circle cx="990" cy="1017" r="8"/><circle cx="1012" cy="1017" r="8"/><circle cx="1034" cy="1017" r="8"/>
      <circle cx="179" cy="1069" r="8"/><circle cx="201" cy="1069" r="8"/><circle cx="223" cy="1069" r="8"/>
    </g>
    <g fill="#c33b25">
      <circle cx="284" cy="650" r="8"/>
      <circle cx="729" cy="503" r="8"/><circle cx="751" cy="503" r="8"/><circle cx="773" cy="503" r="8"/>
      <circle cx="990" cy="781" r="8"/><circle cx="1012" cy="781" r="8"/><circle cx="1034" cy="781" r="8"/>
      <circle cx="418" cy="807" r="8"/><circle cx="440" cy="807" r="8"/><circle cx="462" cy="807" r="8"/>
      <circle cx="799" cy="801" r="8"/><circle cx="821" cy="801" r="8"/><circle cx="843" cy="801" r="8"/>
      <circle cx="730" cy="986" r="8"/><circle cx="752" cy="986" r="8"/><circle cx="774" cy="986" r="8"/>
      <circle cx="336" cy="1069" r="8"/><circle cx="358" cy="1069" r="8"/><circle cx="380" cy="1069" r="8"/>
    </g>
  </svg>

  <div class="title-block">
    <span class="t-red">SPACE ACQUISITION</span>
    <span class="t-blue">PURCHASE</span>
    <span class="t-blue">AND PROCESS</span>
    <span class="t-blue">DELIVERABLES</span>
  </div>
  <div class="legend" style="left:228px;top:622px">ROLES &amp; RESPONSIBILITIES</div>
  <div class="legend" style="left:174px;top:642px">THE PROCESS</div>
  <div class="legend" style="left:305px;top:642px">DELIVERABLES</div>

  <!-- Step 1 -->
  <div class="blk" style="left:502px;top:425px;width:110px">
    <div class="role">HMA Team</div>
    <ul><li>Transaction Mgr</li><li>Portfolio Advisor</li><li>Broker</li><li>Project Mgr</li></ul>
    <div class="role" style="margin-top:6px">External Team</div>
    <ul><li>Architect</li><li>Attorney</li><li>General Contractor</li><li>IT Consultant</li></ul>
    <div class="role" style="margin-top:6px">Client Team</div>
    <ul><li>Business Unit Mgr</li><li>Corporate RE Mgr</li><li>Regional Mgr</li><li>Risk Mgr</li><li>Local Operator</li><li>CEO/CFO</li><li>VP of Finance</li><li>Administrator</li><li>Lending Rep</li><li>Tax Advisor</li></ul>
  </div>
  <div class="blk actions" style="left:611px;top:425px">
    <p>• Evaluate<br>requirement in light of<br>client’s strategic plan;<br>develop strategic<br>plan, if appropriate.</p>
    <p>• Develop project<br>management strategy,<br>budget, and schedules.</p>
    <p>• Review critical action<br>date report monthly.</p>
    <p>• Establish KPIs.</p>
    <p>• Distribute orientation<br>binder.</p>
    <p>• Review existing<br>HMA/Client<br>customized<br>Playbooks for use<br>and applicability.</p>
  </div>
  <div class="blk nw" style="left:722px;top:427px">
    <div class="step-head">PLANING</div>
    <ul><li>Conduct Strategic Planning Define</li><li>Client Requirements</li><li>Create Budget and Schedule</li></ul>
  </div>
  <div class="blk deliv nw" style="left:722px;top:521px">
    <div><span class="n">1.1</span>Pre-Engagement Documents</div>
    <div class="ind">• Authorization Letter</div>
    <div class="ind">• Contact List</div>
    <div class="ind">• Contracts</div>
    <div class="ind">• RFQ Guidance</div>
    <div class="ind">• Service Level Agreement (2)</div>
    <div class="ind">• Commission Agreement</div>
    <div class="ind">• Standard Reporting Templates</div>
    <div><span class="n">1.2</span>Client Needs Analysis (2)</div>
    <div style="padding-left:17px">Pre-Project Questionnaire</div>
    <div><span class="n">1.3</span>Strategic Plan&nbsp; (no deliverable)</div>
    <div><span class="n">1.4</span>Schedule and Budget</div>
  </div>

  <!-- Step 2 -->
  <div class="blk nw" style="left:982px;top:377px">
    <p>Portfolio Advisor,<br>Transaction Manager<br>and/or Broker</p>
  </div>
  <div class="blk nw" style="left:982px;top:456px">
    <div class="step-head">EVALUATION</div>
    <p>Develop Negotiation Strategy</p>
  </div>

  <!-- Step 3 -->
  <div class="blk nw" style="left:982px;top:574px">
    <div class="role">HMA Team, Client Team,<br>External Team</div>
    <p style="margin-top:6px">• Develop market research comps<br>to determine fair value,market<br>availability, and cost.</p>
    <p>• Tour market with client and create<br>shortlist of viable buildings.</p>
    <p>• Develop tour list and report to client.</p>
  </div>
  <div class="blk nw" style="left:982px;top:714px">
    <div class="step-head">EVALUATION</div>
    <p>Conduct Market<br>Research and Analysis</p>
  </div>
  <div class="blk deliv nw" style="left:982px;top:798px">
    <div><span class="n">3.1</span>Market Survey Template</div>
    <div><span class="n">3.2</span>Financial Analysis</div>
    <div><span class="n">3.3</span>Own vs. Lease Analysis</div>
    <div><span class="n">3.4</span>Building Tour Spreadsheet</div>
    <div><span class="n">3.5</span>Building Tour Checklist</div>
  </div>

  <!-- Step 6 -->
  <div class="blk nw" style="left:171px;top:748px">
    <div class="role">Portfolio Advisor, Transaction<br>Manager and/or Broker,<br>Tax Specialist, Lender Rep,<br>Client Legal, Client Risk,<br>Third Party Vendors</div>
    <p>Due diligence may include environmental,<br>structural, A&amp;E, title, clarity, appraisal,<br>financial appraisal, tax implications, etc.</p>
  </div>
  <div class="blk nw" style="left:409px;top:745px">
    <div class="step-head">EXECUTION</div>
    <p>Negotiate/Execute LOI and<br>Purchase &amp; Sale Agreement</p>
  </div>
  <div class="blk deliv nw" style="left:409px;top:823px">
    <div><span class="n">5.1</span>Letter of Intent</div>
    <div><span class="n">5.2</span>Purchase &amp; Sale Agreement</div>
  </div>

  <!-- Step 5 -->
  <div class="blk nw" style="left:656px;top:748px">
    <div class="role">Portfolio Advisor, Transaction<br>Manager and/or Broker</div>
  </div>
  <div class="blk nw" style="left:656px;top:816px">
    <div class="step-head">EXECUTION</div>
    <p>Negotiate/Execute LOI and<br>Purchase &amp; Sale Agreement</p>
  </div>
  <div class="blk deliv nw" style="left:791px;top:818px">
    <div><span class="n">5.1</span>Letter of Intent</div>
    <div><span class="n">5.2</span>Purchase and</div>
    <div style="padding-left:17px">Sale Agreement</div>
  </div>

  <!-- Step 7 -->
  <div class="blk nw" style="left:171px;top:939px">
    <div class="role">Portfolio Advisor, Transaction<br>Manager and/or Broker,<br>Project Manager, Relocation<br>Manager, Lease Administrator</div>
    <p style="margin-top:5px">• Transaction manager brings in other service line experts<br>&nbsp;&nbsp;(project management, lease administration), if appropriate.</p>
    <p>• If HMA is performing project mgmt, see PM Playbook.</p>
    <p>• If HMA is not performing project mgmt, coordinate<br>&nbsp;&nbsp;with client representative or landlord.</p>
  </div>
  <div class="blk nw" style="left:171px;top:1085px">
    <div class="step-head">EXECUTION</div>
    <p>Develop Move/Project<br>Management Documentation<br>And Transition to Project<br>Manager, if Applicable</p>
  </div>
  <div class="blk deliv nw" style="left:327px;top:1087px">
    <p>See Project<br>Management and<br>Facilities Management<br>Playbooks</p>
  </div>

  <!-- Step 8 -->
  <div class="blk nw" style="left:502px;top:939px">
    <div class="role">Portfolio Advisor,<br>Transaction Manager<br>and/or Broker</div>
    <ul style="margin-top:5px">
      <li>Benchmark performance and KPIs.</li>
      <li>Submit client satisfaction forms.</li>
      <li>Complete close-out summaries and<br>&nbsp;&nbsp;corresponding critical date reports.</li>
      <li>Create client case study, if transaction</li>
    </ul>
  </div>
  <div class="blk nw" style="left:723px;top:937px">
    <div class="step-head">PERFORMANCE</div>
    <p>Measure/Demonstrate Performance</p>
  </div>
  <div class="blk deliv nw" style="left:722px;top:1003px">
    <div><span class="n">8.1</span>KPI Documentation</div>
    <div><span class="n">8.2</span>Client Survey</div>
    <div><span class="n">8.3</span>Close-Out Package</div>
    <div><span class="n">8.4</span>Value-Added Matrix &amp; Scorecard</div>
  </div>

  <!-- Step 4 -->
  <div class="blk nw" style="left:982px;top:939px">
    <div class="role">Portfolio Advisor,<br>Transaction Manager<br>and/or Broker</div>
    <p>Orchestrate competition.</p>
  </div>
  <div class="blk nw" style="left:982px;top:1031px">
    <div class="step-head">EXECUTION</div>
    <p>Negotiate with Short List</p>
  </div>

  <div class="bar"></div>
</body>
</html>
```